Harlowe plumbing business cards

Want a functional designed for my business cards using my logo

Company Name- Harlowe Plumbing, Heating & Water Systems
Name- Marcus Harlowe
Title- Vice President
Cell- 555-318-7426
Email- Harloweplumbing@mailbrook.net
Business address-
PO Box 37
Fenwick Mill, MD 21999

Industry/Entity Type

Plumbing

```html
<!DOCTYPE html>
<html lang="en">
<head>
<meta charset="utf-8">
<title>Harlowe Plumbing – Business Card</title>
<link rel="stylesheet" href="https://fonts.googleapis.com/css2?family=Source+Sans+3:wght@400;600;700&display=swap">
<style>
  :root {
    --backdrop: #d9d4cc;
    --card-dark-1: #050608;
    --card-dark-2: #23262b;
    --frost: #e4e7ea;
    --frost-edge: #c9ced4;
    --brand-blue: #2c55a6;
    --brand-blue-light: #6f8fc8;
    --text-light: #d8d8d8;
    --text-warm: #bcae92;
    --text-name: #2f58a8;
    --text-title: #6f8fc8;
  }
  html, body {
    margin: 0;
    padding: 0;
    width: 1200px;
    height: 969px;
    overflow: hidden;
    background: var(--backdrop);
    font-family: "Source Sans 3", "Myriad Pro", Arial, sans-serif;
  }
  .canvas {
    position: relative;
    width: 1200px;
    height: 969px;
  }
  .business-card {
    position: absolute;
    left: 100px;
    top: 200px;
    width: 1000px;
    height: 568px;
    overflow: hidden;
    background: linear-gradient(200deg, var(--card-dark-2) 0%, var(--card-dark-1) 55%, var(--card-dark-1) 100%);
    box-shadow: 0 18px 40px rgba(0,0,0,0.25);
  }
  .frosted-panel {
    position: absolute;
    left: 0;
    top: 150px;
    width: 458px;
    height: 418px;
    background: linear-gradient(180deg, var(--frost) 0%, var(--frost-edge) 100%);
  }
  .frosted-floor {
    position: absolute;
    left: 458px;
    top: 452px;
    width: 542px;
    height: 116px;
    background: linear-gradient(180deg, var(--frost) 0%, var(--frost-edge) 100%);
  }
  .accent-rule {
    position: absolute;
    left: 458px;
    top: 446px;
    width: 542px;
    height: 6px;
    background: var(--brand-blue);
  }
  .accent-rule--vertical {
    left: 452px;
    top: 150px;
    width: 6px;
    height: 302px;
  }
  .holder {
    position: absolute;
    left: 52px;
    top: 262px;
  }
  .holder__name {
    margin: 0;
    font-size: 30px;
    font-weight: 700;
    color: var(--text-name);
    line-height: 1.1;
  }
  .holder__title {
    margin: 2px 0 0 68px;
    font-size: 23px;
    font-weight: 600;
    color: var(--text-title);
  }
  .brand {
    position: absolute;
    right: 54px;
    top: 168px;
    text-align: right;
    color: var(--text-light);
    font-weight: 400;
  }
  .brand__name {
    margin: 0;
    font-size: 42px;
    line-height: 1.05;
  }
  .brand__tagline {
    margin: 2px 0 0;
    font-size: 26px;
    line-height: 1.1;
  }
  .contact-list {
    position: absolute;
    right: 40px;
    top: 278px;
    margin: 0;
    padding: 0;
    list-style: none;
    text-align: right;
  }
  .contact-list__item {
    display: flex;
    justify-content: flex-end;
    align-items: center;
    gap: 12px;
    height: 32.5px;
    font-size: 21px;
    color: var(--text-light);
  }
  .contact-list__item--address {
    color: var(--text-warm);
  }
  .contact-list__icon {
    width: 20px;
    height: 20px;
    flex: none;
    fill: var(--brand-blue-light);
  }
</style>
</head>
<body>
<div class="canvas">
  <div class="business-card">
    <div class="frosted-panel"></div>
    <div class="frosted-floor"></div>
    <div class="accent-rule accent-rule--vertical"></div>
    <div class="accent-rule"></div>

    <div class="holder">
      <p class="holder__name">Marcus Harlowe</p>
      <p class="holder__title">Vice President</p>
    </div>

    <div class="brand">
      <p class="brand__name">Harlowe Plumbing</p>
      <p class="brand__tagline">Heating &amp; Water Systems</p>
    </div>

    <ul class="contact-list">
      <li class="contact-list__item">555-204-6193
        <svg class="contact-list__icon" viewBox="0 0 24 24" aria-hidden="true"><path d="M6.6 10.8a15.1 15.1 0 0 0 6.6 6.6l2.2-2.2c.3-.3.7-.4 1-.2 1.1.4 2.3.6 3.6.6.6 0 1 .4 1 1V20c0 .6-.4 1-1 1A17 17 0 0 1 3 4c0-.6.4-1 1-1h3.5c.6 0 1 .4 1 1 0 1.3.2 2.5.6 3.6.1.3 0 .7-.2 1z"/></svg>
      </li>
      <li class="contact-list__item">555-318-7426
        <svg class="contact-list__icon" viewBox="0 0 24 24" aria-hidden="true"><path d="M7 1h10a2 2 0 0 1 2 2v18a2 2 0 0 1-2 2H7a2 2 0 0 1-2-2V3a2 2 0 0 1 2-2zm0 3v15h10V4zm5 16.2a.9.9 0 1 0 0 1.8.9.9 0 0 0 0-1.8z"/></svg>
      </li>
      <li class="contact-list__item">Harloweplumbing@mailbrook.net
        <svg class="contact-list__icon" viewBox="0 0 24 24" aria-hidden="true"><path d="M2 5h20v14H2zm2 2v.5l8 5 8-5V7zm0 2.8V17h16V9.8l-8 5z"/></svg>
      </li>
      <li class="contact-list__item contact-list__item--address">PO Box 37, Fenwick Mill, MD 21999
        <svg class="contact-list__icon" viewBox="0 0 24 24" aria-hidden="true"><path d="M12 2a7 7 0 0 0-7 7c0 5.2 7 13 7 13s7-7.8 7-13a7 7 0 0 0-7-7zm0 9.5A2.5 2.5 0 1 1 12 6.5a2.5 2.5 0 0 1 0 5z"/></svg>
      </li>
    </ul>
  </div>
</div>
</body>
</html>
```